Book cover entitled #GLOWBEYONDIT

Design front book cover (self-self-portait photos included) for my first book entitled -

#GLOWBEYONDIT (may be best to have different shades of colour for glow beyond it to stand off you). I'm intentionally choosing a title that is essentially a hashtag.

Subtitle - Rewriting quiet inner battles

Concept of cover - left side of my face is shaded with shame and right side is brighter and hopeful. I have also include my logo.

Link for photos
https://www.filqorvex.com/sh/tq7mxd2kw9pl41a/BBR8NpXwQ3hLm6TzvKe2YUJ5b?dl=0

Target Market(s)

People (or friends & family) suffering with the shame of mental health struggles

Industry/Entity Type

Mental Health

Font styles to use
Other font styles liked:
• Avenir

Colors
3276b5
85acd3
cfdeed

Requirements
Must have
• Relatable, contemporary, authentic & compelling
• Link for photos
• https://www.filqorvex.com/sh/tq7mxd2kw9pl41a/BBR8NpXwQ3hLm6TzvKe2YUJ5b?dl=0
Nice to have
• Abstract & creative
Should not have
• Cheesy, plastic, pedestrian etc

```html
<!DOCTYPE html>
<html lang="en">
<head>
<meta charset="utf-8">
<title>#GLOWBEYONDIT — Book Cover</title>
<link rel="stylesheet" href="https://fonts.googleapis.com/css2?family=Nunito+Sans:wght@400;600&family=Oswald:wght@300;400&display=swap">
<style>
  :root {
    --cover-blue: #2f5191;
    --cover-blue-deep: #263f76;
    --cover-blue-soft: #3a5fa0;
    --brand-blue: #3276b5;
    --mist-blue: #85acd3;
    --ice-blue: #cfdeed;
    --frame-pale: #d3e4e2;
    --ornament-tone: #9fc0d4;
    --badge-cream: #f4ead0;
    --photo-shadow: #1c2838;
    --photo-cool: #4d6176;
    --photo-warm-dark: #5a4a3e;
    --photo-warm: #b08e72;
  }
  * { margin: 0; padding: 0; box-sizing: border-box; }
  html, body {
    width: 800px; height: 1200px; overflow: hidden;
    background: var(--cover-blue);
  }
  .cover {
    position: relative; width: 800px; height: 1200px; overflow: hidden;
    background: radial-gradient(ellipse at 50% 40%, var(--cover-blue-soft) 0%, var(--cover-blue) 55%, var(--cover-blue-deep) 100%);
  }
  .cover-art { position: absolute; inset: 0; width: 800px; height: 1200px; }
  .author-name {
    position: absolute; top: 298px; left: 0; width: 800px;
    text-align: center;
    font-family: "Nunito Sans", "Avenir", sans-serif;
    font-weight: 400; font-size: 32px; line-height: 40px; letter-spacing: 1px;
    color: var(--ice-blue);
  }
  .author-name .first { color: #4a8fd0; }
  .publisher-badge {
    position: absolute; left: 400px; top: 888px;
    width: 92px; height: 92px;
    transform: translate(-50%, -50%) rotate(45deg);
    background: var(--badge-cream);
  }
  .publisher-name {
    position: absolute; left: 340px; top: 888px; width: 120px;
    transform: translateY(-50%);
    text-align: center;
    font-family: "Nunito Sans", "Avenir", sans-serif;
    font-weight: 600; font-size: 15px; line-height: 1;
    color: var(--brand-blue);
  }
  .book-title {
    position: absolute; top: 985px; left: 0; width: 800px;
    text-align: center;
    font-family: "Oswald", "Avenir Next Condensed", sans-serif;
    font-weight: 400; font-size: 106px; line-height: 110px;
    letter-spacing: 3px;
    color: var(--ice-blue);
  }
  .book-subtitle {
    position: absolute; top: 1098px; left: 0; width: 800px;
    text-align: center;
    font-family: "Oswald", "Avenir Next Condensed", sans-serif;
    font-weight: 300; font-size: 40px; line-height: 36px;
    letter-spacing: 1.5px; text-transform: uppercase;
    color: var(--ice-blue);
  }
</style>
</head>
<body>
<main class="cover">
  <svg class="cover-art" viewBox="0 0 800 1200" xmlns="http://www.w3.org/2000/svg">
    <defs>
      <linearGradient id="portraitSplit" x1="0" y1="0" x2="1" y2="0">
        <stop offset="0" stop-color="var(--photo-shadow)"/>
        <stop offset="0.499" stop-color="var(--photo-cool)"/>
        <stop offset="0.501" stop-color="var(--photo-warm-dark)"/>
        <stop offset="1" stop-color="var(--photo-warm)"/>
      </linearGradient>
      <radialGradient id="portraitVignette" cx="0.5" cy="0.5" r="0.55">
        <stop offset="0.45" stop-color="#000" stop-opacity="0"/>
        <stop offset="1" stop-color="#000" stop-opacity="0.45"/>
      </radialGradient>
    </defs>

    <g class="corner-ornaments" fill="var(--ornament-tone)" fill-opacity="0.16">
      <polygon points="40,36 340,36 40,352" role="img" aria-label="Scrollwork ornament, top left corner"/>
      <polygon points="760,36 460,36 760,352" role="img" aria-label="Scrollwork ornament, top right corner"/>
      <polygon points="40,590 40,930 320,930" role="img" aria-label="Scrollwork ornament, lower left corner"/>
      <polygon points="760,590 760,930 480,930" role="img" aria-label="Scrollwork ornament, lower right corner"/>
    </g>

    <polygon class="portrait-frame" points="400,72 778,474 400,876 22,474" fill="var(--frame-pale)"/>
    <g class="portrait" role="img" aria-label="Author self-portrait split down the middle: left half in cool blue shadow, right half warm and bright">
      <polygon points="400,81 769,474 400,867 31,474" fill="url(#portraitSplit)"/>
      <polygon points="400,81 769,474 400,867 31,474" fill="url(#portraitVignette)"/>
    </g>
  </svg>

  <p class="author-name"><span class="first">THEO</span> VARDEN</p>

  <div class="publisher-badge"></div>
  <p class="publisher-name">theo varden</p>

  <h1 class="book-title">#GLOWBEYONDIT</h1>
  <p class="book-subtitle">Rewriting quiet<br>inner battles</p>
</main>
</body>
</html>
```